Retirement Plan Advisor Bio

See the attached document and photo for content. I would like someone to design this one page flyer using my logo. This logo was designed by a designer with sketch hive. I am looking for a professional looking document. I want to he color scheme to be primarily white and gold.

Target Market(s)

Employers who offer a retirement plan

Requirements
Should not have
• The designs that I have received look more like resumes. I am interested in advertising my Retirement plan services. If anyone can change their submissions and change it to an ad for retirement plan services instead of a Bio or resume, I would prefer that.

```html
<!DOCTYPE html>
<html lang="en">
<head>
<meta charset="utf-8">
<title>Retirement Plan Advisor Flyer</title>
<link href="https://fonts.googleapis.com/css2?family=Arimo:wght@400;700&family=Montserrat:wght@300;400;500;600;700&display=swap" rel="stylesheet">
<style>
:root{
  --brown:#3a2c20;
  --brown-dark:#33271c;
  --gold:#c8a063;
  --gold-light:#e8c77f;
  --gold-text:#b98e55;
  --ink:#2b2b2b;
  --white:#ffffff;
}
*{margin:0;padding:0;box-sizing:border-box}
html,body{width:928px;height:1200px;overflow:hidden;background:var(--white)}
.flyer{position:relative;width:928px;height:1200px;font-family:"Montserrat",sans-serif;color:var(--ink)}
.hero-photo{position:absolute;left:313px;top:0;width:615px;height:398px;
  background:linear-gradient(90deg,rgba(255,255,255,1) 0%,rgba(255,255,255,0) 22%),
  linear-gradient(160deg,#d9c3a8 0%,#b89c7e 35%,#8a7058 60%,#e3d6c6 100%)}
.brand{position:absolute;left:24px;top:60px;display:flex;align-items:center;gap:14px}
.brand-dot{width:34px;height:34px;border-radius:50%;background:var(--gold)}
.brand-name{font-family:"Montserrat",sans-serif;font-weight:500;font-size:31px;color:var(--gold-text);letter-spacing:.5px}
.contact{position:absolute;left:53px;top:204px;font-family:"Arimo",sans-serif;color:var(--ink)}
.contact .web{font-size:36px;line-height:40px;margin-bottom:8px}
.contact p{font-size:20px;line-height:28px}
.title-band{position:absolute;left:0;top:398px;width:928px;height:57px;background:var(--brown);
  border-top:3px solid var(--gold);border-bottom:3px solid var(--gold);
  display:flex;align-items:center;justify-content:center}
.title-band h1{font-weight:700;font-size:26px;color:var(--white)}
.service{position:absolute;top:486px;width:272px}
.service h2{height:65px;background:var(--brown);color:var(--white);font-weight:700;font-size:16.5px;
  line-height:22px;display:flex;align-items:center;justify-content:center;text-align:center;
  box-shadow:0 8px 8px -4px rgba(0,0,0,.25)}
.service p{margin:22px 20px 0;font-weight:400;font-size:13.5px;line-height:16.4px;color:#333}
.s1{left:35px}.s2{left:332px}.s3{left:628px}
.about{position:absolute;left:0;top:742px;width:928px;height:458px;background:var(--brown)}
.about .rule{position:absolute;left:0;width:928px;height:3px;background:linear-gradient(90deg,var(--gold),var(--gold-light),var(--gold))}
.portrait{position:absolute;left:59px;top:53px;width:224px;height:288px;
  background:radial-gradient(circle at 50% 40%,#d8b98a 0%,#8c7a72 45%,#4e5f85 100%)}
.advisor-name{position:absolute;left:53px;top:357px;width:236px;border-top:2px solid var(--gold);border-bottom:2px solid var(--gold);
  padding:3px 0 4px;font-weight:600;font-size:16.5px;line-height:25px;color:var(--gold-text);white-space:nowrap}
.advisor-name sup{font-size:7px}
.timeline{position:absolute;left:336px;top:0}
.timeline svg{position:absolute;left:-12px;top:0}
.entry{position:absolute;left:25px;width:540px;font-family:"Arimo",sans-serif;color:var(--gold-text)}
.entry h3{font-weight:700;font-size:15.5px;margin-bottom:8px;letter-spacing:.2px}
.lead{font-size:13.8px;line-height:15.2px;max-width:528px}
.small{font-size:11.6px;line-height:15.2px;max-width:410px}
.list li{list-style:none;font-size:11.8px;line-height:19px}
.edu strong{font-size:11.8px;display:block;margin-bottom:6px}
.disclaimer{font-size:11px;line-height:14.6px;white-space:nowrap}
</style>
</head>
<body>
<main class="flyer">
  <div class="hero-photo" role="img" aria-label="Photo of a smiling retired couple at a kitchen table with a laptop and coffee"></div>
  <div class="brand"><span class="brand-dot"></span><span class="brand-name">Evenfield Financial, LLC</span></div>
  <div class="contact">
    <div class="web">www.janeholloway.com</div>
    <p>2400 Marlow Rd. | Brookvale, IL 60999</p>
    <p>(555)204.7391</p>
    <p>jane.holloway@evenfield.com</p>
  </div>

  <header class="title-band"><h1>Financial Planning Services</h1></header>

  <section class="service s1"><h2>RETIREMENT PLANNING</h2>
    <p>My strategies help you assemble the pieces of this puzzle into an plan. Your vision can be pursued.</p></section>
  <section class="service s2"><h2>INVESTMENT<br>MANAGEMENT</h2>
    <p>Assessing your risk level and matching it up with a portfolio of investments is key to building your nest egg as well as making it last. My job is to help you live out your retirement years with a sense of financial independence.</p></section>
  <section class="service s3"><h2>RETIREMENT PLAN<br>DEVELOPMENT</h2>
    <p>Designing a plan that will benefit, both, the employees as well as the employer, choosing a lineup of world class investments, keeping cost down and keeping up with industry regulation all play a part in improving participant outcome. My experience brings experience in all these areas.</p></section>

  <section class="about">
    <div class="rule" style="top:21px"></div>
    <div class="rule" style="top:434px"></div>
    <div class="portrait" role="img" aria-label="Portrait photo of the financial advisor"></div>
    <div class="advisor-name">Jane R Holloway CFP<sup>®</sup>AIF<sup>®</sup><br>Northmark Financial Advisor</div>

    <div class="timeline">
      <svg width="24" height="360" viewBox="0 0 24 360" aria-hidden="true">
        <line x1="12" y1="58" x2="12" y2="343" stroke="var(--gold)" stroke-width="2"/>
        <g fill="var(--brown)" stroke="var(--gold)" stroke-width="5">
          <circle cx="12" cy="58" r="9"/><circle cx="12" cy="134" r="9"/>
          <circle cx="12" cy="219" r="9"/><circle cx="12" cy="343" r="9"/>
        </g>
      </svg>
      <div class="entry" style="top:47px"><p class="lead">Over 18 years of experience in the retirement plan industry Focused on helping plan sponsors reduce administrative burdens and fiduciary risk Dedicated to helping employees work toward a positive retirement outcome through careful analysis of their savings rate, investment strategy and overall financial&nbsp; wellness</p></div>
      <div class="entry" style="top:125px"><h3>PROFESSIONAL SPECIALTIES</h3>
        <p class="small">I strive to improve retirement outcomes for my plan sponsor clients and their employees through careful retirement plan design assistance, strategic and targeted communication and education , as well as continual monitoring of results.</p></div>
      <div class="entry" style="top:210px"><h3>QUALIFICATIONS</h3>
        <ul class="list"><li>Certified Financial Planner®</li><li>Accredited Investment Fiduciary®</li><li>Investment Advisor Representative</li><li>Series 7, 63, and 65 Securities licenses with Northmark Financial</li><li>Holds Life and Health Insurance licenses from Illinois</li></ul></div>
      <div class="entry edu" style="top:334px"><h3>EDUCATION</h3>
        <strong>BS Westbrook University, 1987</strong>
        <p class="disclaimer">*Securities and Investment Advisory Services offered through<br>Northmark Financial Holdings, Inc, a Registered Broker/Dealer and Investment Advisor, member NFRA/SIPA</p></div>
    </div>
  </section>
</main>
</body>
</html>
```